Professional & attention grabbing.

A business card design, front and back. I already have a logo I will attach, but I am open to something new as well.
Things to include:
Name:
Title:
Phone:
Email:
Wanting something that is professional but attention grabbing.
Also we do a lot of work using drones on natural gas pipelines (leading the future)if you want to include any of that. I'm open to ideas.
Target Market(s)
Natural gas transmission industry / greenhouse gas mitigation industry
Industry/Entity Type
Business
Contact Information for Business Card
All details have been conveyed above.
Colors
Designer to choose colors to be used in the design.
Look and feel
Each slider illustrates characteristics of the customer's brand and the style your logo design should communicate.

```html
<!DOCTYPE html>
<html lang="en">
<head>
<meta charset="utf-8">
<title>Kestrel Inspections — Business Card</title>
<link rel="stylesheet" href="https://fonts.googleapis.com/css2?family=Jost:wght@400;500;700&display=swap">
<style>
  :root {
    --bg: #e6e7e9;
    --card: #ffffff;
    --ink: #2a2a2a;
    --muted: #6b6b6b;
    --brand-red: #d4121d;
    --brand-red-dark: #b50d17;
  }
  * { box-sizing: border-box; margin: 0; padding: 0; }
  html, body {
    width: 1200px; height: 1200px; overflow: hidden;
    background: var(--bg);
    font-family: "Jost", Arial, sans-serif;
  }
  .canvas {
    width: 1200px; height: 1200px;
    display: flex; flex-direction: column;
    align-items: center; justify-content: center; gap: 80px;
  }
  .card {
    position: relative;
    width: 720px; height: 411px;
    background: var(--card);
    box-shadow: 0 6px 18px rgba(0,0,0,0.12);
    overflow: hidden;
  }
  .brand {
    display: flex; align-items: center; gap: 12px;
    color: var(--ink); font-weight: 700;
  }
  .brand-mark { background: var(--brand-red); display: block; }
  .front .brand { position: absolute; left: 46px; top: 48px; font-size: 30px; }
  .front .brand-mark { width: 22px; height: 22px; }
  .person { position: absolute; left: 430px; top: 118px; }
  .person-name { color: var(--brand-red); font-size: 30px; font-weight: 500; line-height: 1.1; }
  .person-title { color: var(--muted); font-size: 17px; margin-top: 2px; }
  .contact {
    position: absolute; left: 330px; top: 194px;
    border-left: 1.5px solid var(--brand-red);
    padding-left: 14px;
    color: var(--muted); font-size: 18px; line-height: 1.3;
  }
  .contact-group + .contact-group { margin-top: 10px; }
  .contact-row { display: flex; align-items: flex-start; gap: 8px; }
  .contact-row svg { width: 15px; height: 15px; margin-top: 4px; flex: none; fill: var(--brand-red); }
  .contact-indent { padding-left: 23px; }
  .band { position: absolute; left: 0; bottom: 0; width: 720px; height: 60px; }
  .back { display: flex; align-items: center; justify-content: center; }
  .back .brand { font-size: 46px; gap: 16px; }
  .back .brand-mark { width: 32px; height: 32px; }
</style>
</head>
<body>
<main class="canvas">

  <section class="card front" aria-label="Card front">
    <div class="brand"><span class="brand-mark"></span>Kestrel Inspections</div>

    <div class="person">
      <p class="person-name">John Doe</p>
      <p class="person-title">Director</p>
    </div>

    <div class="contact">
      <div class="contact-group">
        <div class="contact-row">
          <svg viewBox="0 0 16 16"><path d="M8 1 1 7.5h2V15h4v-4h2v4h4V7.5h2z"/></svg>
          <span>Dummy City</span>
        </div>
        <div class="contact-indent">Dummy country land</div>
      </div>
      <div class="contact-group">
        <div class="contact-row">
          <svg viewBox="0 0 16 16"><path d="M2 5c0-2 2-3 6-3s6 1 6 3v1h-3.5V4.5h-5V6H2zM4 8h8l1.5 6h-11zM8 9.5a2 2 0 1 0 0 4 2 2 0 0 0 0-4z"/></svg>
          <span>123-456-7890</span>
        </div>
        <div class="contact-row">
          <svg viewBox="0 0 16 16"><path d="M8 1a7 7 0 1 0 0 14A7 7 0 0 0 8 1zm0 1.4c.7.7 1.4 2 1.7 3.6H6.3C6.6 4.4 7.3 3.1 8 2.4zM2.6 7.3h2.5v1.4H2.6zm8.3 0h2.5v1.4h-2.5zm-4.6 0h3.4v1.4H6.3zM6.3 10h3.4c-.3 1.6-1 2.9-1.7 3.6-.7-.7-1.4-2-1.7-3.6z"/></svg>
          <span>www.kestrelinspect.com</span>
        </div>
        <div class="contact-row">
          <svg viewBox="0 0 16 16"><path d="M1 3h14v10H1zm1.5 1.3v.4L8 8.6l5.5-3.9v-.4z"/></svg>
          <span>john@kestrelinspect.com</span>
        </div>
      </div>
    </div>

    <svg class="band" viewBox="0 0 720 60" preserveAspectRatio="none" aria-hidden="true">
      <polygon points="250,6 720,6 720,24 242,24" fill="var(--brand-red)"/>
      <polygon points="236,31 720,31 720,60 224,60" fill="var(--brand-red-dark)"/>
    </svg>
  </section>

  <section class="card back" aria-label="Card back">
    <div class="brand"><span class="brand-mark"></span>Kestrel Inspections</div>
  </section>

</main>
</body>
</html>
```